Rack Card for Portuguese Walking Food Tour

I would like a vertical rack card measuring 99x210mm. Here is the information I would like to include. It does not need to be in this format. We are located in Setubal, Portugal.
Please use the attached Teal Heron Logo.
Setúbal: Tradition and Today
Experience the culinary delights of Setúbal, Portugal with a walking food tour around our waterfront village. Discover the Mercado da Gaivota Branca, voted one of the world’s best markets by Metro Ledger, and indulge in local wines and dishes. Prepare for a calm stroll on flat streets. No hills to climb on this tour.
Duration: 4 hours
www.brinebasketwalks.com
+351 265 000 487

```html
<!DOCTYPE html>
<html lang="en">
<head>
<meta charset="utf-8">
<title>Teal Heron Tours – Setúbal Rack Card</title>
<link rel="stylesheet" href="https://fonts.googleapis.com/css2?family=Kaushan+Script&family=Montserrat:wght@600;700;800&family=Raleway:wght@400&display=swap">
<style>
  :root{
    --orange:#f26722;
    --orange-deep:#d64f0e;
    --white:#ffffff;
    --photo-wine:#7a6a5a;
    --photo-fish:#d9735e;
    --photo-oyster:#c9c7c2;
    --photo-meat:#b3703f;
    --photo-market:#b39a78;
  }
  *{margin:0;padding:0;box-sizing:border-box}
  html,body{width:1200px;height:2545px;overflow:hidden;background:var(--orange)}
  .card{position:relative;width:1200px;height:2545px;overflow:hidden;background:var(--orange)}
  .backdrop,.photos{position:absolute;left:0;top:0;width:1200px;height:2545px}
  .brand{position:absolute;left:150px;top:170px;display:flex;align-items:center;gap:34px}
  .brand-dot{width:190px;height:190px;border-radius:50%;background:var(--white)}
  .brand-name{font-family:'Montserrat',sans-serif;font-weight:700;color:var(--white);font-size:92px;line-height:1;letter-spacing:1px}
  .brand-name span{display:block;font-size:62px;letter-spacing:12px;margin-top:14px;text-align:right}
  .title{position:absolute;left:0;width:1200px;text-align:center;color:var(--white)}
  .title-script{top:545px;font-family:'Kaushan Script',cursive;font-size:150px;line-height:1.1}
  .title-main{top:700px;font-family:'Montserrat',sans-serif;font-weight:800;font-size:86px;letter-spacing:-1px;line-height:1}
  .rule{position:absolute;left:492px;top:822px;width:228px;height:20px;border-radius:10px;background:var(--white)}
  .intro{position:absolute;left:146px;top:880px;width:908px;font-family:'Raleway',sans-serif;font-size:45px;line-height:76px;color:var(--white);text-align:justify}
  .info{position:absolute;left:148px;top:1552px;font-family:'Montserrat',sans-serif;font-weight:700;color:var(--orange)}
  .info p{font-size:50px;line-height:58px}
  .phone{position:absolute;left:56px;top:1700px;display:flex;align-items:center;gap:28px;font-family:'Montserrat',sans-serif;font-weight:600;font-size:66px;color:var(--orange)}
  .phone svg{width:66px;height:66px}
</style>
</head>
<body>
<main class="card">
  <svg class="backdrop" viewBox="0 0 1200 2545" aria-hidden="true">
    <rect width="1200" height="2545" fill="var(--orange-deep)"/>
    <circle cx="470" cy="840" r="600" fill="var(--orange)"/>
    <circle cx="110" cy="780" r="500" fill="var(--orange-deep)"/>
    <path d="M1200 1500 L1200 2545 L380 2545 L380 2020 Z" fill="var(--orange-deep)"/>
    <path d="M60 1830 L60 110 Q60 56 116 56 L1086 56 Q1142 56 1142 112 L1142 1690" fill="none" stroke="var(--white)" stroke-width="8"/>
    <path d="M0 1528 L745 1528 A144 144 0 0 1 745 1816 L0 1816 Z" fill="var(--white)"/>
    <path d="M0 1540 L740 1540 A132 132 0 0 1 740 1804 L0 1804" fill="none" stroke="var(--orange)" stroke-width="7"/>
  </svg>

  <div class="brand">
    <div class="brand-dot"></div>
    <div class="brand-name">Teal Heron<span>TOURS</span></div>
  </div>

  <h1 class="title title-script">Setúbal</h1>
  <h2 class="title title-main">TRADITION &amp; TODAY</h2>
  <div class="rule"></div>

  <p class="intro">Experience the culinary delights of Setúbal, Portugal with a walking food tour around our waterfront village. Discover the Mercado da Gaivota Branca, voted one of the world’s best markets by Metro Ledger, and indulge in local wines and dishes. Prepare for a calm stroll on flat streets. No hills to climb on this tour.</p>

  <div class="info">
    <p>Duration: 4 hours</p>
    <p>www.brinebasketwalks.com</p>
  </div>
  <div class="phone">
    <svg viewBox="0 0 24 24" aria-hidden="true"><path fill="var(--orange)" d="M6.6 10.8c1.4 2.8 3.8 5.2 6.6 6.6l2.2-2.2c.3-.3.7-.4 1-.2 1.1.4 2.3.6 3.6.6.6 0 1 .4 1 1V20c0 .6-.4 1-1 1C10.6 21 3 13.4 3 4c0-.6.4-1 1-1h3.5c.6 0 1 .4 1 1 0 1.3.2 2.5.6 3.6.1.3 0 .7-.2 1z"/><path fill="none" stroke="var(--orange)" stroke-width="1.8" stroke-linecap="round" d="M14 3.5a7 7 0 0 1 6.5 6.5M14 7a3.5 3.5 0 0 1 3 3"/></svg>
    <span>+351 265 000 487</span>
  </div>

  <svg class="photos" viewBox="0 0 1200 2545">
    <g stroke="var(--white)" stroke-width="14">
      <rect role="img" aria-label="Photo: glasses of beer and white wine on a café terrace table" x="-180" y="2010" width="580" height="580" rx="70" transform="rotate(45 110 2300)" fill="var(--photo-wine)"/>
      <rect role="img" aria-label="Photo: market stall with sacks of dried beans and price tags" x="420" y="2435" width="470" height="470" rx="60" transform="rotate(45 655 2670)" fill="var(--photo-market)"/>
      <rect role="img" aria-label="Photo: fresh red mullet on ice at the fish market" x="590" y="2025" width="210" height="210" rx="40" transform="rotate(45 695 2130)" fill="var(--photo-fish)"/>
      <rect role="img" aria-label="Photo: sliced chorizo and toasted bread" x="870" y="2240" width="440" height="440" rx="60" transform="rotate(45 1090 2460)" fill="var(--photo-meat)"/>
      <rect role="img" aria-label="Photo: fresh oysters on ice with lemon wedges" x="870" y="1740" width="440" height="440" rx="60" transform="rotate(45 1090 1960)" fill="var(--photo-oyster)"/>
    </g>
  </svg>
</main>
</body>
</html>
```